Managed Service Provider email

We need an email designed that advertises our Managed Services product. We have been in business 28 years. Managed Services includes proactive ticketing, Help desk support, server and workstation monitoring, data backup monitoring, spam protection, regular reports, Deskflow 240, telecom services, ISP management, vendor management and more.

Target Market(s)

Business owners, decision makers, IT, CTO

Industry/Entity Type

Information Technology

Colors

Designer to choose colors to be used in the design.

Requirements
Must have
• Bullet points with included services. Mention of 28 years in business.
Nice to have
• We'd love our designer to read up on what an MSP (Managed Service Provider) does and use that information to find/create content for our email project.
Should not have
• A picture of a computer with a thermometer in its mouth.

```html
<!DOCTYPE html>
<html lang="en">
<head>
<meta charset="utf-8">
<title>Vantel Network Services – Managed Services</title>
<link href="https://fonts.googleapis.com/css2?family=Montserrat:wght@400;500;600;700&display=swap" rel="stylesheet">
<style>
:root{
  --blue:#1e88dc;
  --blue-dark:#0f5fae;
  --ink:#2f3336;
  --muted:#555b60;
  --white:#ffffff;
  --band-dark:#1a2730;
  --band-mid:#2b3d48;
  --tile:#2d3134;
  --tile-light:#3a3f43;
  --hero-deep:#0a1a5c;
  --hero-mid:#1b3ea8;
}
*{box-sizing:border-box;margin:0;padding:0}
html,body{width:1200px;height:3571px;overflow:hidden;background:var(--white)}
body{font-family:'Montserrat',Arial,sans-serif;color:var(--ink)}
.canvas{position:relative;width:1200px;height:3571px;overflow:hidden;background:var(--white)}
.abs{position:absolute}

/* header */
.brand{display:flex;align-items:center;gap:12px;font-weight:700;color:var(--ink);white-space:nowrap}
.brand-mark{width:16px;height:16px;background:var(--blue);flex:none}
.header-brand{left:150px;top:72px;font-size:22px;line-height:30px}
.contact{display:flex;align-items:center;gap:14px;top:62px;font-size:19px;line-height:28px;text-align:right;color:var(--ink);white-space:nowrap}
.contact-phone{right:467px}
.contact-address{right:150px}
.contact-icon{width:46px;height:46px;border:3px solid var(--blue);border-radius:12px;display:flex;align-items:center;justify-content:center;flex:none}

/* hero */
.hero{left:150px;top:152px;width:900px;height:538px;
  background:radial-gradient(ellipse at 55% 25%,#3f7be0 0%,var(--hero-mid) 30%,var(--hero-deep) 70%,#050a2a 100%);
  display:flex;flex-direction:column;align-items:center;justify-content:center;text-align:center}
.hero-title{font-size:48px;line-height:58px;font-weight:700;color:var(--white);margin-top:-30px}
.hero-title .accent{color:var(--blue)}
.hero-tagline{margin-top:14px;font-size:20px;font-weight:500;color:var(--white);letter-spacing:.5px}
.hero-button{margin-top:22px;background:var(--blue);color:var(--white);font-size:17px;font-weight:600;padding:16px 32px;border-radius:8px;letter-spacing:.5px}

/* section title */
.section-title{left:0;top:740px;width:1200px;text-align:center;font-size:40px;letter-spacing:18px;font-weight:500;color:var(--ink)}
.section-title .accent{color:var(--blue)}
.section-rule{left:569px;top:837px;width:62px;height:3px;background:var(--ink)}

/* feature cards */
.feature{width:270px;top:900px;text-align:center}
.feature-box{height:180px;background:var(--blue);display:flex;align-items:center;justify-content:center;box-shadow:0 14px 28px rgba(0,0,0,.18)}
.feature-label{margin-top:22px;font-size:27px;line-height:33px;color:var(--ink)}

/* dark band */
.band{left:0;top:1262px;width:1200px;height:957px;
  background:radial-gradient(ellipse at 70% 60%,var(--band-mid) 0%,var(--band-dark) 65%,#101a20 100%)}
.photo{width:524px;height:239px}
.photo-datacenter{background:linear-gradient(180deg,#2c2c2c 0%,#777 45%,#9a9a98 60%,#1d1d1d 100%)}
.photo-security{background:linear-gradient(90deg,#0b0f14 0%,#1c2e44 45%,#3b5c80 70%,#10171f 100%)}
.photo-laptop{background:linear-gradient(135deg,#f2f2f2 0%,#cfd3d6 45%,#8b929a 70%,#e8e8e8 100%)}
.band-text{font-size:38px;line-height:46px;font-weight:500;color:var(--white)}

/* service tiles */
.tile{width:420px}
.tile-box{height:238px;background:linear-gradient(180deg,var(--tile-light),var(--tile));display:flex;align-items:center;justify-content:center}
.tile-label{margin-top:22px;text-align:center;font-size:27px;font-weight:500;color:var(--ink)}

/* partners */
.partners{left:0;top:2971px;width:1200px;height:239px;
  background:radial-gradient(ellipse at 15% 50%,#1d5aa8 0%,#0e2a66 40%,#081640 100%);
  display:flex;align-items:center;justify-content:center;gap:70px}
.badge-square{width:115px;height:120px;background:#e9ecef;border-radius:6px}
.badge-circle{width:120px;height:120px;border-radius:50%;background:var(--blue)}
.badge-wide{width:170px;height:90px;background:rgba(255,255,255,.9);border-radius:4px}
.badge-long{width:260px;height:60px;background:rgba(255,255,255,.9);border-radius:4px}

/* footer */
.footer-brand{left:0;top:3300px;width:1200px;justify-content:center;font-size:46px}
.footer-brand .brand-mark{width:28px;height:28px}
.copyright{left:0;top:3448px;width:1200px;text-align:center;font-size:21px;color:var(--muted);line-height:36px}
.copyright .credit{color:var(--blue);font-weight:600}
</style>
</head>
<body>
<div class="canvas">

  <header>
    <div class="abs brand header-brand"><span class="brand-mark"></span>Vantel Network Services</div>
    <div class="abs contact contact-phone">
      <div>555-201-0404<br>555-201-5554</div>
      <div class="contact-icon">
        <svg width="24" height="24" viewBox="0 0 24 24" fill="none" stroke="#1e88dc" stroke-width="2.2" stroke-linejoin="round"><path d="M5 3h4l2 5-2.5 1.5a11 11 0 0 0 6 6L16 13l5 2v4a2 2 0 0 1-2 2A17 17 0 0 1 3 5a2 2 0 0 1 2-2z"/></svg>
      </div>
    </div>
    <div class="abs contact contact-address">
      <div>1480 W Maple Ave<br>Riverton, MO 65010</div>
      <div class="contact-icon">
        <svg width="24" height="24" viewBox="0 0 24 24" fill="none" stroke="#1e88dc" stroke-width="2.2"><path d="M12 22s7-7 7-12a7 7 0 0 0-14 0c0 5 7 12 7 12z"/><circle cx="12" cy="10" r="2.5"/></svg>
      </div>
    </div>
  </header>

  <section class="abs hero" role="img" aria-label="Glowing blue fibre-optic strands and network lines">
    <h1 class="hero-title">Our <span class="accent">Managed</span><br>Services Product</h1>
    <p class="hero-tagline">28 years in business</p>
    <div class="hero-button">READ MORE</div>
  </section>

  <h2 class="abs section-title">MANAGED <span class="accent">SERVICES</span></h2>
  <div class="abs section-rule"></div>

  <div class="abs feature" style="left:150px">
    <div class="feature-box">
      <svg width="100" height="120" viewBox="0 0 100 120" fill="none" stroke="#fff" stroke-width="5" stroke-linejoin="round" stroke-linecap="round">
        <path d="M20 8h38l18 18v34"/><path d="M58 8v18h18"/><path d="M20 8v90h28"/>
        <path d="M58 112V62a6 6 0 0 1 12 0v26l18 4a6 6 0 0 1 5 7l-4 13"/>
      </svg>
    </div>
    <div class="feature-label">Includes Proactive<br>Ticketing</div>
  </div>
  <div class="abs feature" style="left:465px">
    <div class="feature-box">
      <svg width="110" height="120" viewBox="0 0 110 120" fill="none" stroke="#fff" stroke-width="6" stroke-linecap="round">
        <path d="M20 62V52a35 35 0 0 1 70 0v10"/>
        <rect x="12" y="58" width="18" height="30" rx="6" fill="#fff"/>
        <rect x="80" y="58" width="18" height="30" rx="6" fill="#fff"/>
        <path d="M89 88v8a14 14 0 0 1-14 14H60"/>
        <rect x="46" y="104" width="16" height="12" rx="5" fill="#fff"/>
      </svg>
    </div>
    <div class="feature-label">Help Desk Support</div>
  </div>
  <div class="abs feature" style="left:780px">
    <div class="feature-box">
      <svg width="190" height="120" viewBox="0 0 190 120" fill="none" stroke="#fff" stroke-width="7" stroke-linejoin="round">
        <rect x="6" y="8" width="120" height="82" rx="4"/><path d="M52 90v16M80 90v16M38 110h56"/>
        <rect x="140" y="8" width="42" height="104" rx="4"/><path d="M150 28h22M150 44h22M150 60h22"/>
      </svg>
    </div>
    <div class="feature-label">Server and<br>Workstation<br>Monitoring</div>
  </div>

  <section class="abs band">
    <div class="abs photo photo-datacenter" style="left:150px;top:59px" role="img" aria-label="Corridor of server racks in a data centre"></div>
    <div class="abs band-text" style="left:736px;top:132px">Data Backup<br>Monitoring</div>

    <div class="abs band-text" style="left:200px;top:432px;width:267px;text-align:right">Spam<br>Protection</div>
    <div class="abs photo photo-security" style="left:526px;top:359px" role="img" aria-label="Screen showing the word security with a pointer"></div>

    <div class="abs photo photo-laptop" style="left:150px;top:659px" role="img" aria-label="Hands typing on a laptop showing report charts"></div>
    <div class="abs band-text" style="left:736px;top:732px">Regular<br>Reports</div>
  </section>

  <div class="abs tile" style="left:150px;top:2281px">
    <div class="tile-box"><div style="width:120px;height:120px;background:var(--blue)"></div></div>
    <div class="tile-label">Deskflow 240</div>
  </div>
  <div class="abs tile" style="left:630px;top:2281px">
    <div class="tile-box">
      <svg width="110" height="150" viewBox="0 0 110 150" fill="none" stroke="#1e88dc" stroke-width="6" stroke-linecap="round" stroke-linejoin="round">
        <circle cx="55" cy="34" r="7" fill="#1e88dc"/>
        <path d="M38 18a24 24 0 0 0 0 32M72 18a24 24 0 0 1 0 32M26 8a38 38 0 0 0 0 52M84 8a38 38 0 0 1 0 52"/>
        <path d="M55 44L30 144M55 44l25 100M44 88h22M40 108l30 20M70 108l-30 20"/>
      </svg>
    </div>
    <div class="tile-label">Telecom Services</div>
  </div>
  <div class="abs tile" style="left:150px;top:2612px">
    <div class="tile-box">
      <svg width="180" height="140" viewBox="0 0 180 140" fill="none" stroke="#1e88dc" stroke-width="6" stroke-linejoin="round">
        <rect x="62" y="6" width="56" height="34" rx="6"/>
        <path d="M90 40v30M30 70h120M30 70v30M90 70v30M150 70v30" stroke-dasharray="6 6"/>
        <rect x="6" y="100" width="48" height="32" rx="6"/><rect x="66" y="100" width="48" height="32" rx="6"/><rect x="126" y="100" width="48" height="32" rx="6"/>
      </svg>
    </div>
    <div class="tile-label">ISP Management</div>
  </div>
  <div class="abs tile" style="left:630px;top:2612px">
    <div class="tile-box">
      <svg width="200" height="120" viewBox="0 0 200 120" fill="#1e88dc">
        <path d="M4 30l40-22 26 12-40 60z"/><path d="M196 30l-40-22-26 12 40 60z"/>
        <path d="M60 28l40-10 50 16 14 40-44 36-12-8-10 6-12-8-10 4-14-12-14-6z"/>
      </svg>
    </div>
    <div class="tile-label">Vendor Management</div>
  </div>

  <section class="abs partners" role="group" aria-label="Technology partners">
    <div class="badge-square"></div>
    <div class="badge-circle"></div>
    <div class="badge-wide"></div>
    <div class="badge-long"></div>
  </section>

  <footer>
    <div class="abs brand footer-brand"><span class="brand-mark"></span>Vantel Network Services</div>
    <p class="abs copyright">© Copyright - Vantel Network Services 2018 | Privacy Policy<br>Built By <span class="credit">Brightline Studio</span></p>
  </footer>

</div>
</body>
</html>
```